Mobile Recording Studio needs business cards

Open to seeing a creative design, but I want to emphasis my logo and minimize the name/title and company information. Possible a fully black background on card.

My company is a mobile sound recording studio. ok to include a my trailer (actual or cartoon) on the card. My initial thought is more straight forward, but a good design will win me over.

SPECS:
CMYK color mode
High (300ppi) raster effect.
cover bleed area
please deliver: Illustrator file with layers and a pdf at completion.

Name and info for the business card:

Mitchell Garvey
ADR Mixer

email: Mitchell@TakebayDub.example

address:
418 - 6057 East Pembury
Vancouver, BC V3R 2T4

phone:
604.419.8827 office

website:
www.TakebayDub.example

FB: @TakebayDub

Instagram: @TheTakebayDub

Industry/Entity Type

Television Production

Contact Information for Business Card

Mitchell Garvey
ADR Mixer

email: Mitchell@TakebayDub.example

address:
418 - 6057 East Pembury
Vancouver, BC V3R 2T4

phone:
604.419.8827 office

website:
www.TakebayDub.example

FB: @TakebayDub

Instagram: @TheTakebayDub

Colors

Designer to choose colors to be used in the design.

Requirements
Must have
• emphasis my logo and minimize the name/title and company information.
• SPECS:
• CMYK color mode
• High (300ppi) raster effect.
• cover bleed area
• please deliver: Illustrator file with layers and a pdf at completion.
Nice to have
• maybe include the following:
• all black background or black theme
• my work trailer (actual or cartoon) refer to Instagram: @TheTakebayDub

```html
<!DOCTYPE html>
<html lang="en">
<head>
<meta charset="utf-8">
<title>TakebayDub Business Cards</title>
<link href="https://fonts.googleapis.com/css2?family=Poppins:wght@300;400;600;800&display=swap" rel="stylesheet">
<style>
  :root{
    --stage:#2a2a2a;
    --card-dark:#141414;
    --card-mid:#242424;
    --silver:#d6d6d6;
    --silver-light:#f2f2f2;
    --silver-dark:#9a9a9a;
    --ink:#0d0d0d;
    --info:#e4e4e4;
  }
  *{margin:0;padding:0;box-sizing:border-box}
  html,body{width:1200px;height:960px;overflow:hidden;background:var(--stage)}
  body{position:relative;font-family:"Poppins",sans-serif}
  .card{
    position:absolute;left:230px;width:740px;height:423px;overflow:hidden;
    background:
      repeating-linear-gradient(0deg,rgba(255,255,255,.018) 0 1px,transparent 1px 3px),
      linear-gradient(160deg,var(--card-mid),var(--card-dark) 60%,#0b0b0b);
    box-shadow:0 14px 30px rgba(0,0,0,.55);
  }
  .card--front{top:38px}
  .card--back{top:499px}
  .brand{
    font-family:"Poppins",sans-serif;font-weight:600;color:var(--silver);
    letter-spacing:.02em;white-space:nowrap;display:flex;align-items:center;
  }
  .brand__mark{display:inline-block;border-radius:50%;background:var(--silver)}
  .card--front .brand{position:absolute;left:0;right:0;top:160px;justify-content:center;font-size:70px;gap:18px}
  .card--front .brand__mark{width:26px;height:26px}
  .card--back .brand{position:absolute;left:118px;top:88px;font-size:40px;gap:12px}
  .card--back .brand__mark{width:15px;height:15px}
  .contact{position:absolute;left:120px;top:258px;color:var(--info);font-weight:300;font-size:14.5px;line-height:1.3}
  .contact__row{display:flex;align-items:flex-start;gap:10px;margin-bottom:10px}
  .contact__icon{width:13px;height:13px;flex:none;margin-top:3px}
  .nameplate{
    position:absolute;right:0;top:176px;width:262px;height:76px;
    clip-path:polygon(14% 0,100% 0,100% 100%,0 100%);
    background:
      repeating-linear-gradient(0deg,rgba(0,0,0,.04) 0 1px,transparent 1px 3px),
      linear-gradient(100deg,var(--silver-dark),var(--silver-light) 45%,var(--silver) 75%,var(--silver-dark));
    text-align:right;padding:14px 26px 0 0;color:var(--ink);
  }
  .nameplate__name{font-weight:800;font-size:21px;letter-spacing:.01em;line-height:1.1}
  .nameplate__title{font-weight:400;font-size:12px;margin-top:2px}
</style>
</head>
<body>
  <section class="card card--front" aria-label="Card front">
    <div class="brand"><span class="brand__mark"></span>TakebayDub</div>
  </section>

  <section class="card card--back" aria-label="Card back">
    <div class="brand"><span class="brand__mark"></span>TakebayDub</div>

    <div class="contact">
      <div class="contact__row">
        <svg class="contact__icon" viewBox="0 0 12 12" aria-hidden="true"><path d="M6 .5a4 4 0 0 1 4 4c0 3-4 7-4 7s-4-4-4-7a4 4 0 0 1 4-4z" fill="none" stroke="#e4e4e4" stroke-width="1.1"/><circle cx="6" cy="4.5" r="1.4" fill="#e4e4e4"/></svg>
        <div>418 - 6057 East Pembury<br>Vancouver, BC V3R 2T4</div>
      </div>
      <div class="contact__row">
        <svg class="contact__icon" viewBox="0 0 12 12" aria-hidden="true"><path d="M2.5 1h2l1 2.5-1.3 1a6 6 0 0 0 3.3 3.3l1-1.3L11 7.5v2a1.5 1.5 0 0 1-1.5 1.5A8.5 8.5 0 0 1 1 2.5 1.5 1.5 0 0 1 2.5 1z" fill="#e4e4e4"/></svg>
        <div>604.419.8827</div>
      </div>
      <div class="contact__row">
        <svg class="contact__icon" viewBox="0 0 12 12" aria-hidden="true"><circle cx="6" cy="6" r="5" fill="#e4e4e4"/></svg>
        <div>@TheTakebayDub</div>
      </div>
    </div>

    <div class="nameplate">
      <div class="nameplate__name">MITCHELL GARVEY</div>
      <div class="nameplate__title">ADR Mixer</div>
    </div>
  </section>
</body>
</html>
```